Home Services Website Design and Revisions

We have started to create a website but I would like to get some ideas and a quote on how to create a more professional website then what we have created thus far.

http://brindlehomeworks.example/

Pages I would need on the site

Home page - company summary and brand promise
who we are
what we do - services offered
our promise to quality and client experience
client experiences - testimonials and pictures
Promotions
Career opportunities - Join The team
Updates

Target Market(s)

Homeowners in the DFW region

Industry/Entity Type

Home Improvement

Number of Pages Required

5+ page

Font styles to use
Sans Serif

Requirements
Must have
• Home page - company summary and brand promise
• who we are
• what we do - services offered
• our promise to quality and client experience
• client experiences - testimonials and pictures
• Promotions
• Career opportunities - Join The team
• logo
• pictures
• links to social media sites
• A very impactful home page
• With a image of home and family.
• a beautiful home, yard and pictures of a loving family smiling and enjoying their home.
Nice to have
• Pictures with people to create emotion
• we don't work on houses
• we work on homes with families that trust us to provide quality services in a timely manner
• Families that trust us as their partner when they need work at their home with their family
Should not have
• low quality images or images just of homes

```html
<!DOCTYPE html>
<html lang="en">
<head>
<meta charset="utf-8">
<title>Brindle Homeworks — Home Services</title>
<link href="https://fonts.googleapis.com/css2?family=Montserrat:wght@400;600;700;800&family=Open+Sans:wght@400;600;700&family=Lora:ital@1&display=swap" rel="stylesheet">
<style>
:root{
  --green:#8dc63f;
  --green-dark:#7ab52f;
  --green-mid:#86bf38;
  --navy:#1f2442;
  --navy-deep:#161a30;
  --ink:#222;
  --muted:#777;
  --light:#f3f4f6;
  --white:#fff;
  --line:#e3e3e3;
}
*{box-sizing:border-box;margin:0;padding:0}
html,body{width:1200px;height:5056px;overflow:hidden}
body{position:relative;background:var(--white);font-family:"Open Sans",Arial,sans-serif;color:var(--ink)}
.abs{position:absolute}
.photo{position:absolute}
.serif-italic{font-family:"Lora",Georgia,serif;font-style:italic}

/* top bar */
.topbar{top:0;left:0;width:1200px;height:34px;background:var(--navy);display:flex;align-items:center;justify-content:space-between;padding:0 80px;font-size:11px;color:#cfd3e0}
.topbar .contact{display:flex;gap:22px;align-items:center}
.topbar .contact span{display:flex;gap:6px;align-items:center}
.socials{display:flex;gap:8px}
.socials i{width:20px;height:20px;border-radius:50%;background:var(--green);display:block}

/* nav */
.nav{top:34px;left:0;width:1200px;height:101px;display:flex;align-items:center;justify-content:space-between;padding:0 80px}
.brand{display:flex;align-items:center;gap:10px;font-family:"Montserrat",sans-serif;font-weight:800;font-size:24px;color:var(--navy)}
.brand i{width:22px;height:22px;background:var(--green);display:block}
.menu{display:flex;gap:34px;align-items:center;font-family:"Montserrat",sans-serif;font-size:13px;font-weight:600;color:#444}
.menu .active{color:var(--ink);border-bottom:3px solid var(--green);padding-bottom:6px;margin-top:9px}

/* hero */
.hero{top:135px;left:0;width:1200px;height:691px;background:linear-gradient(100deg,#4b6a3a 0%,#7d9a63 35%,#c9b7a3 60%,#e6d8cf 100%)}
.hero-copy{top:388px;left:80px;color:var(--white)}
.hero-copy .kicker{font-family:"Montserrat",sans-serif;font-weight:700;font-size:15px;letter-spacing:1px}
.hero-copy h1{font-family:"Montserrat",sans-serif;font-weight:800;font-size:56px;line-height:1.05;margin-top:6px}
.hero-copy p{font-family:"Lora",serif;font-style:italic;font-size:15px;line-height:1.6;margin-top:12px;width:300px}
.hero-arrow{width:26px;height:26px;border-radius:50%;background:rgba(0,0,0,.35);display:flex;align-items:center;justify-content:center;top:470px}
.dots{display:flex;gap:7px}
.dots i{width:9px;height:9px;border-radius:50%;border:2px solid #fff;display:block}
.dots i.on{background:#fff}

/* service tiles */
.tiles{top:792px;left:54px;width:1092px;height:236px;display:flex}
.tile{flex:1;display:flex;align-items:center;justify-content:center;text-align:center;color:#fff;font-family:"Montserrat",sans-serif;font-weight:700;font-size:13px;line-height:1.5;margin-top:34px;height:185px;border-right:1px solid rgba(255,255,255,.25)}
.tile.first{margin-top:0;height:236px;background:var(--green)}
.tile:nth-child(2){background:var(--green-mid)}
.tile:nth-child(3){background:#82ba35}
.tile:nth-child(4){background:#7eb532}
.tile:nth-child(5){background:var(--green-dark);border-right:0}

/* intro */
.intro-photo{top:1062px;left:472px;width:256px;height:175px;background:linear-gradient(180deg,#a9bccd 0%,#8a8478 55%,#5f6b4a 100%)}
.intro-text{top:1274px;left:70px;width:1060px;text-align:center;font-size:15px;line-height:1.55;color:#333}
.btn{display:inline-block;background:var(--green);color:#fff;font-family:"Montserrat",sans-serif;font-weight:700;font-size:10px;letter-spacing:.5px;padding:9px 22px}
.intro-btn{top:1453px;left:545px}
.rule{top:1418px;left:545px;width:110px;height:1px;background:var(--line)}

/* call band */
.call{top:1523px;left:0;width:1200px;height:337px;background:var(--navy)}
.call h3{position:absolute;top:52px;width:100%;text-align:center;color:#fff;font-family:"Montserrat",sans-serif;font-size:20px;font-weight:700}
.call .phone{position:absolute;top:122px;left:364px;width:472px;height:135px;background:var(--green);display:flex;align-items:center;justify-content:center;gap:18px;color:#fff;font-family:"Montserrat",sans-serif;font-weight:800;font-size:52px}

/* section titles */
.sec-title{left:0;width:1200px;text-align:center;font-family:"Montserrat",sans-serif;font-weight:700;font-size:28px;line-height:36px;color:var(--ink)}
.sec-sub{left:0;width:1200px;text-align:center;font-family:"Lora",serif;font-style:italic;font-size:12px;line-height:16px;color:#999}
.sec-title::after{content:"";display:block;width:60px;height:2px;background:var(--green);margin:8px auto 0}

/* what we do */
.svc{width:330px}
.svc h4{font-family:"Montserrat",sans-serif;font-size:17px;font-weight:700;color:var(--ink);margin-bottom:10px}
.svc p{font-size:13px;line-height:1.6;color:var(--muted)}
.svc.left{text-align:right}
.svc-icon{width:46px;height:46px;border-radius:50%;background:#e6e6e6;display:flex;align-items:center;justify-content:center}
.wwd-photo{top:2090px;left:438px;width:320px;height:421px;background:radial-gradient(ellipse at 50% 45%,#d96aa3 0%,#b0c3d1 45%,#ffffff 75%)}

/* work */
.work{top:2561px;left:0;width:1200px;height:607px;background:var(--light)}
.gallery{top:2804px;left:0;width:1200px;height:246px;display:flex}
.gallery div{flex:1}

/* testimonial */
.testi{top:3168px;left:0;width:1200px;height:364px;background:var(--navy);color:#fff}
.avatar{position:absolute;top:40px;left:563px;width:74px;height:74px;border-radius:50%;background:#b9a08a;border:3px solid #fff}
.testi blockquote{position:absolute;top:134px;left:190px;width:820px;text-align:center;font-family:"Lora",serif;font-style:italic;font-size:15px;line-height:1.6}
.testi .who{position:absolute;top:240px;width:100%;text-align:center}
.testi .who b{display:block;font-family:"Montserrat",sans-serif;font-size:16px}
.testi .who span{font-size:12px;color:#aab}
.testi .pn{position:absolute;top:146px;font-family:"Montserrat",sans-serif;font-size:12px;font-weight:700}

/* why choose */
.card{width:347px}
.card .pic{height:169px}
.card h4{font-family:"Montserrat",sans-serif;font-size:17px;font-weight:700;margin:42px 0 14px}
.card p{font-size:13px;line-height:1.6;color:var(--muted);margin-bottom:28px}

/* cta */
.cta{top:4347px;left:0;width:1200px;height:135px;background:var(--green);display:flex;align-items:center;justify-content:center;font-family:"Montserrat",sans-serif;font-weight:700;font-size:28px;color:#fff}
.cta b{color:var(--navy);margin-left:10px}

/* footer */
.footer{top:4482px;left:0;width:1200px;height:472px;background:var(--navy-deep);color:#c8ccda}
.foot-col{position:absolute;top:50px}
.foot-col h5{font-family:"Montserrat",sans-serif;font-size:16px;color:#fff;margin-bottom:8px}
.foot-col h5::after{content:"";display:block;width:40px;height:2px;background:var(--green);margin-top:10px}
.foot-col ul{list-style:none;margin-top:22px}
.foot-col li{font-size:13px;margin-bottom:16px;display:flex;gap:12px;align-items:center}
.foot-col li::before{content:"›";color:#fff}
.touch-item{margin-top:22px;font-size:13px;line-height:1.6}
.touch-item b{display:flex;gap:10px;align-items:center;color:#fff;font-size:13px}
.foot-person{top:4448px;left:67px;width:253px;height:472px;background:linear-gradient(180deg,#5c7fa8 0%,#3c5e86 50%,#2a3147 100%)}
.bottombar{top:4954px;left:0;width:1200px;height:102px;background:#11142a;display:flex;align-items:center;justify-content:space-between;padding:0 67px;color:#b3b8c8;font-size:12px}
.bottombar .brand{color:#fff;font-size:20px}
</style>
</head>
<body>

<div class="abs topbar">
  <div class="contact">
    <span><svg width="12" height="12" viewBox="0 0 24 24"><path fill="#8dc63f" d="M6.6 10.8a15 15 0 0 0 6.6 6.6l2.2-2.2c.3-.3.7-.4 1-.2 1.1.4 2.3.6 3.6.6.6 0 1 .4 1 1V20c0 .6-.4 1-1 1A17 17 0 0 1 3 4c0-.6.4-1 1-1h3.5c.6 0 1 .4 1 1 0 1.3.2 2.5.6 3.6.1.3 0 .7-.2 1z"/></svg>214 555 0187</span>
    <span><svg width="13" height="10" viewBox="0 0 26 20"><rect x="1" y="1" width="24" height="18" fill="none" stroke="#8dc63f" stroke-width="2"/><path d="M1 1l12 10L25 1" fill="none" stroke="#8dc63f" stroke-width="2"/></svg>info@brindlehomeworks.example</span>
  </div>
  <div class="socials"><i></i><i></i><i></i><i></i><i></i><i></i></div>
</div>

<header class="abs nav">
  <div class="brand"><i></i>Brindle</div>
  <nav class="menu">
    <span class="active">HOME</span><span>PAGES</span><span>PORTFOLIO</span><span>BLOG</span><span>CONTACT</span><span>SHORTCODES</span>
    <svg width="14" height="14" viewBox="0 0 24 24"><circle cx="10" cy="10" r="7" fill="none" stroke="#444" stroke-width="2.5"/><path d="M15 15l6 6" stroke="#444" stroke-width="2.5"/></svg>
  </nav>
</header>

<section class="photo hero" role="img" aria-label="Smiling woman holding a basket of pink flowers in a bright greenhouse"></section>
<div class="abs hero-copy">
  <div class="kicker">START YOUR OWN</div>
  <h1>BUSINESS<br>NOW.</h1>
  <p>Sed ut perspiciatis unde omnis iste natus error sit voluptatem accusantium.</p>
</div>
<div class="abs hero-arrow" style="left:24px"><svg width="10" height="10" viewBox="0 0 10 10"><path d="M7 1L3 5l4 4" fill="none" stroke="#fff" stroke-width="2"/></svg></div>
<div class="abs hero-arrow" style="right:24px"><svg width="10" height="10" viewBox="0 0 10 10"><path d="M3 1l4 4-4 4" fill="none" stroke="#fff" stroke-width="2"/></svg></div>
<div class="abs dots" style="top:776px;left:572px"><i class="on"></i><i></i><i></i></div>

<div class="abs tiles">
  <div class="tile first">EXTERIOR<br>PAINTING</div>
  <div class="tile">INTERIOR PAINTING</div>
  <div class="tile">WINDOW<br>WASHING</div>
  <div class="tile">LAWN MOWING<br>LANDSCAPING</div>
  <div class="tile">FREE<br>ESTIMATE</div>
</div>

<div class="photo intro-photo" role="img" aria-label="Freshly painted two-storey family home with a garage"></div>
<p class="abs intro-text serif-italic">A fresh paint job has the power to totally transform the look of your house in less time and for less cash than any other remodeling project. That thin skin of resin and pigment also protects your investment, shielding it from sun, wind, and rain—until the paint begins to crack and peel, that is. Then it's time to button up with a couple of new coats. Brindle would provided you with a top-quality materials. Nothing welcomes family and friends and clients like a fresh coat of paint.</p>
<div class="abs rule"></div>
<span class="abs btn intro-btn">READ MORE</span>

<section class="abs call">
  <h3>CONTACT YOUR HOME SERVICE PROVIDER NOW!</h3>
  <div class="phone"><svg width="44" height="44" viewBox="0 0 24 24"><path fill="#fff" d="M6.6 10.8a15 15 0 0 0 6.6 6.6l2.2-2.2c.3-.3.7-.4 1-.2 1.1.4 2.3.6 3.6.6.6 0 1 .4 1 1V20c0 .6-.4 1-1 1A17 17 0 0 1 3 4c0-.6.4-1 1-1h3.5c.6 0 1 .4 1 1 0 1.3.2 2.5.6 3.6.1.3 0 .7-.2 1z"/></svg>214 555 0187</div>
</section>

<h2 class="abs sec-title" style="top:1962px">What We Do</h2>

<div class="abs svc left" style="top:2090px;left:30px"><h4>Exterior residential painting</h4><p>Quisque in mi vestibulum, mattis neque sit amet, pulvinar mi. Nunc quis sem nisi vitae lectus tincidunt.</p></div>
<div class="abs svc-icon" style="top:2082px;left:377px"><svg width="18" height="18" viewBox="0 0 24 24"><path d="M4 20l4-1 11-11-3-3L5 16z" fill="#fff"/></svg></div>
<div class="abs svc left" style="top:2240px;left:30px"><h4>Interior residential painting</h4><p>Sed ut perspiciatis unde omnis iste natus error sit voluptatem accusantium doloremque duis.</p></div>
<div class="abs svc-icon" style="top:2232px;left:377px"><svg width="18" height="18" viewBox="0 0 24 24"><path d="M4 20l4-1 11-11-3-3L5 16z" fill="#fff"/></svg></div>
<div class="abs svc left" style="top:2396px;left:30px"><h4>Commercial painting</h4><p>Aenean nec fermentum lectus. Donec placerat justo in neque scelerisque, id semper est.</p></div>
<div class="abs svc-icon" style="top:2388px;left:377px"><svg width="18" height="18" viewBox="0 0 24 24"><path d="M4 20l4-1 11-11-3-3L5 16z" fill="#fff"/></svg></div>

<div class="photo wwd-photo" role="img" aria-label="Smiling gardener holding a pink watering can and a potted plant"></div>

<div class="abs svc-icon" style="top:2082px;left:792px"><svg width="18" height="18" viewBox="0 0 24 24"><path d="M4 20l4-1 11-11-3-3L5 16z" fill="#fff"/></svg></div>
<div class="abs svc" style="top:2090px;left:870px"><h4>Condominium and Apartment painting</h4><p>Nam sapien erat, congue at purus dignissim, blandit porta urna. Nam neque metus mollis.</p></div>
<div class="abs svc-icon" style="top:2257px;left:792px"><svg width="18" height="18" viewBox="0 0 24 24"><path d="M4 20l4-1 11-11-3-3L5 16z" fill="#fff"/></svg></div>
<div class="abs svc" style="top:2262px;left:870px"><h4>Fence Staining</h4><p>Vestibulum varius in orci at fringilla. Morbi imperdiet, ligula ut bibendum convallis dolor sed.</p></div>
<div class="abs svc-icon" style="top:2412px;left:792px"><svg width="18" height="18" viewBox="0 0 24 24"><path d="M4 20l4-1 11-11-3-3L5 16z" fill="#fff"/></svg></div>
<div class="abs svc" style="top:2417px;left:870px"><h4>Landscaping services</h4><p>Mauris pellentesque diam nec ex efficitur fermentum. Praesent eu nulla nibh cras varius in sed.</p></div>

<section class="abs work"></section>
<h2 class="abs sec-title" style="top:2650px">This is our Work</h2>
<div class="abs sec-sub" style="top:2704px">Portfolio Showcase</div>
<div class="abs gallery">
  <div class="photo" style="position:static;background:linear-gradient(160deg,#b5c2cc,#8c5f4b)" role="img" aria-label="Victorian house exterior with paint colour swatches"></div>
  <div class="photo" style="position:static;background:linear-gradient(160deg,#c7d0d8,#a08a74)" role="img" aria-label="Large stone family home"></div>
  <div class="photo" style="position:static;background:linear-gradient(160deg,#e6ddd0,#9a7c5e)" role="img" aria-label="Freshly painted living room interior"></div>
  <div class="photo" style="position:static;background:linear-gradient(160deg,#d9cbb5,#8a6e50)" role="img" aria-label="Empty room with new wood floor"></div>
  <div class="photo" style="position:static;background:linear-gradient(160deg,#8fb36a,#4c6b35)" role="img" aria-label="Landscaped garden with flowering shrubs"></div>
  <div class="photo" style="position:static;background:linear-gradient(160deg,#9cc074,#3f5e2c)" role="img" aria-label="Lawn and garden beds after landscaping"></div>
</div>
<div class="abs dots" style="top:3086px;left:588px"><i class="on" style="border-color:#8dc63f;background:#8dc63f"></i><i style="border-color:#ccc"></i></div>

<section class="abs testi">
  <div class="avatar" role="img" aria-label="Customer portrait"></div>
  <span class="pn" style="left:64px">PREV</span>
  <blockquote>Lorem ipsum dolor sit amet, consectetur adipiscing elit. Nunc ut imperdiet purus. Donec ac pretium nunc. Vestibulum id aliquam urna. Proin sed convallis dui. Maecenas eget massa quis mi fringilla porta. Sed at augue at orci posuere tempor. Aenean feugiat odio est, eget tristique lectus ullamcorper sit amet.</blockquote>
  <span class="pn" style="right:64px">NEXT</span>
  <div class="who"><b>Dana Whitfield</b><span>Customer</span></div>
</section>

<h2 class="abs sec-title" style="top:3614px">Why choose us?</h2>
<div class="abs sec-sub" style="top:3668px">Take a look</div>

<article class="abs card" style="top:3774px;left:67px">
  <div class="pic" role="img" aria-label="Hands planting young flowers in soil" style="background:linear-gradient(160deg,#9bbf6e,#6b4a32)"></div>
  <h4>We care about you</h4>
  <p>Lorem ipsum dolor sit amet, consectetur adipiscing elit. Cras hendrerit odio quis viverra tristique. Donec non nisl duis arcu consequat lacinia ut in.</p>
  <span class="btn">READ MORE</span>
</article>
<article class="abs card" style="top:3774px;left:428px">
  <div class="pic" role="img" aria-label="Smiling gardener trimming a hedge" style="background:linear-gradient(160deg,#a7c58a,#4f6e3a)"></div>
  <h4>Build with passion</h4>
  <p>Sed fringilla ullamcorper est id sollicitudin. Proin venenatis a elit in vulputate. Nullam non libero ullamcorper, pulvinar felis vel, cursus eros.</p>
  <span class="btn">READ MORE</span>
</article>
<article class="abs card" style="top:3774px;left:792px">
  <div class="pic" role="img" aria-label="Team member tending plants in a greenhouse" style="background:linear-gradient(160deg,#b9d09a,#5a7a42)"></div>
  <h4>Creative Team</h4>
  <p>Proin faucibus laoreet urna, in venenatis enim porttitor a. Duis malesuada ullamcorper semper. Pellentesque sollicitudin pharetra est sollicitudin.</p>
  <span class="btn">READ MORE</span>
</article>

<section class="abs cta">Are you ready for the time of your life? <b>Buy Launchpad now!</b></section>

<footer class="abs footer">
  <div class="foot-col" style="left:337px">
    <h5>Usefull Links</h5>
    <ul><li>Support Center (Faq)</li><li>Pricing</li><li>Features Overview</li><li>Welcome Page</li><li>Under Maintenance</li><li>Testimonials</li></ul>
  </div>
  <div class="foot-col" style="left:613px;width:260px">
    <h5>Get in Touch</h5>
    <div class="touch-item"><b><svg width="14" height="16" viewBox="0 0 24 28"><path d="M12 0a9 9 0 0 0-9 9c0 7 9 19 9 19s9-12 9-19a9 9 0 0 0-9-9zm0 13a4 4 0 1 1 0-8 4 4 0 0 1 0 8z" fill="#8dc63f"/></svg>Address</b>418 Cedar Hollow Lane, Plano, TX 75023</div>
    <div class="touch-item"><b><svg width="14" height="14" viewBox="0 0 24 24"><path fill="#8dc63f" d="M6.6 10.8a15 15 0 0 0 6.6 6.6l2.2-2.2c.3-.3.7-.4 1-.2 1.1.4 2.3.6 3.6.6.6 0 1 .4 1 1V20c0 .6-.4 1-1 1A17 17 0 0 1 3 4c0-.6.4-1 1-1h3.5c.6 0 1 .4 1 1 0 1.3.2 2.5.6 3.6.1.3 0 .7-.2 1z"/></svg>Phone / Fax</b>+214 555 0142 &nbsp;|&nbsp; +214 555 0143</div>
    <div class="touch-item"><b><svg width="15" height="12" viewBox="0 0 26 20"><rect x="1" y="1" width="24" height="18" fill="none" stroke="#8dc63f" stroke-width="2"/><path d="M1 1l12 10L25 1" fill="none" stroke="#8dc63f" stroke-width="2"/></svg>Email</b>info@brindlehomeworks.example</div>
  </div>
  <div class="foot-col" style="left:886px;width:250px">
    <h5>Latest Posts</h5>
    <div role="img" aria-label="Gardener kneeling beside a planted flower bed" style="margin-top:22px;width:170px;height:118px;background:linear-gradient(160deg,#9fc27a,#4d6a35)"></div>
    <div style="font-size:11px;margin-top:12px">22 February 2015</div>
    <div style="font-family:Montserrat,sans-serif;font-weight:700;color:#fff;font-size:13px;margin-top:4px">Planting &amp; Removal</div>
    <div style="display:flex;gap:80px;font-size:11px;font-weight:700;margin-top:18px;color:#fff"><span>PREV</span><span>NEXT</span></div>
  </div>
</footer>
<div class="photo foot-person" role="img" aria-label="Landscaper in a blue plaid shirt holding a shovel"></div>

<div class="abs bottombar">
  <div class="brand"><i></i>Brindle</div>
  <div>Terms of use &nbsp;|&nbsp; Help Center &nbsp;|&nbsp; Contact Us &nbsp;|&nbsp; Brindle 2015 © All Rights Reserved</div>
</div>

</body>
</html>
```